Wedding Dried Apple Label / Name Place Card

We are looking for a simple but stylish label to be attached via string to a bag of dried apples from my family's fruit farm. The size of the label we think should be similar to the size of a business card. The packaging will be a plastic bag: 4" x 2" x 6".
We would like it to say something like:
Remy & Joss
Est. Sept 10, 2017
Dried Apple Slices
Product of Quenton Fruit Farm
________________
(We need a spot to write in the name of the person and a table number)
Our colors are also grey and navy, and would like these colors to be used.
We have uploaded a photo of the plastic bag.
Wedding

```html
<!DOCTYPE html>
<html lang="en">
<head>
<meta charset="utf-8">
<title>Remy &amp; Joss – Dried Apple Label</title>
<link href="https://fonts.googleapis.com/css2?family=Montserrat:wght@600&family=Herr+Von+Muellerhoff&display=swap" rel="stylesheet">
<style>
  :root {
    --paper: #f6f5ef;
    --navy: #2c3d68;
    --wash-teal: rgba(110, 185, 178, 0.55);
    --wash-aqua: rgba(90, 190, 212, 0.45);
    --wash-mint: rgba(165, 212, 202, 0.5);
    --wash-grey: rgba(150, 158, 165, 0.35);
    --hole: #ffffff;
  }
  html, body {
    margin: 0;
    padding: 0;
    width: 686px;
    height: 1200px;
    overflow: hidden;
    background: var(--paper);
  }
  .label {
    position: relative;
    width: 686px;
    height: 1200px;
    background: var(--paper);
    overflow: hidden;
    font-family: "Montserrat", sans-serif;
    color: var(--navy);
  }
  .wash {
    position: absolute;
    pointer-events: none;
  }
  .wash--top {
    left: -60px;
    top: -40px;
    width: 560px;
    height: 780px;
    background:
      radial-gradient(ellipse 140px 110px at 320px 80px, var(--wash-teal), transparent 70%),
      radial-gradient(ellipse 190px 160px at 130px 170px, var(--wash-mint), transparent 72%),
      radial-gradient(ellipse 160px 180px at 110px 360px, var(--wash-aqua), transparent 72%),
      radial-gradient(ellipse 110px 90px at 150px 400px, var(--wash-grey), transparent 70%),
      radial-gradient(ellipse 170px 150px at 380px 330px, var(--wash-mint), transparent 72%),
      radial-gradient(ellipse 150px 140px at 220px 600px, var(--wash-teal), transparent 72%),
      radial-gradient(ellipse 120px 130px at 420px 500px, var(--wash-mint), transparent 70%);
  }
  .wash--bottom {
    left: 230px;
    top: 880px;
    width: 480px;
    height: 360px;
    background:
      radial-gradient(ellipse 160px 110px at 260px 90px, var(--wash-mint), transparent 72%),
      radial-gradient(ellipse 140px 120px at 380px 180px, var(--wash-teal), transparent 72%),
      radial-gradient(ellipse 110px 90px at 330px 170px, var(--wash-grey), transparent 70%),
      radial-gradient(ellipse 170px 120px at 180px 290px, var(--wash-mint), transparent 72%),
      radial-gradient(ellipse 90px 70px at 400px 130px, var(--wash-aqua), transparent 70%);
  }
  .tag-hole {
    position: absolute;
    left: 312px;
    top: 57px;
    width: 68px;
    height: 68px;
    border-radius: 50%;
    background: var(--hole);
    box-shadow: inset 0 3px 4px rgba(0, 0, 0, 0.25);
  }
  .est-date {
    position: absolute;
    top: 180px;
    left: 0;
    width: 100%;
    text-align: center;
    font-size: 32px;
    letter-spacing: 6px;
    margin: 0;
    font-weight: 600;
  }
  .couple-names {
    position: absolute;
    left: 0;
    top: 0;
    width: 100%;
    margin: 0;
    font-family: "Herr Von Muellerhoff", cursive;
    font-weight: 400;
    color: var(--navy);
  }
  .couple-names__line {
    position: absolute;
    white-space: nowrap;
    line-height: 1;
    transform: rotate(-6deg);
  }
  .couple-names__line--first {
    left: 95px;
    top: 240px;
    font-size: 230px;
  }
  .couple-names__line--second {
    left: 170px;
    top: 460px;
    font-size: 230px;
  }
  .couple-names__amp {
    font-size: 150px;
    margin-right: 10px;
  }
  .product {
    position: absolute;
    top: 787px;
    left: 0;
    width: 100%;
    text-align: center;
    margin: 0;
    font-size: 23px;
    line-height: 40px;
    letter-spacing: 4.6px;
    font-weight: 600;
  }
  .write-line {
    position: absolute;
    left: 87px;
    width: 506px;
    height: 1px;
    background: var(--navy);
  }
  .write-line--guest { top: 994px; }
  .write-line--table { top: 1143px; }
</style>
</head>
<body>
  <main class="label">
    <div class="wash wash--top" role="img" aria-label="Soft teal and grey watercolour wash"></div>
    <div class="wash wash--bottom" role="img" aria-label="Soft teal and grey watercolour wash"></div>
    <div class="tag-hole"></div>

    <p class="est-date">EST. SEPT 10, 2017</p>

    <h1 class="couple-names">
      <span class="couple-names__line couple-names__line--first">Remy</span>
      <span class="couple-names__line couple-names__line--second"><span class="couple-names__amp">&amp;</span>Joss</span>
    </h1>

    <p class="product">DRIED APPLE SLICES<br>PRODUCT OF QUENTON FRUIT FARM</p>

    <div class="write-line write-line--guest" aria-label="Guest name"></div>
    <div class="write-line write-line--table" aria-label="Table number"></div>
  </main>
</body>
</html>
```